Coffee and fruit juice

We are a malaysian restaurant that also serves aussie coffee and breakfast from 7am to 11am. After 11am we serve malaysian food but we also have a salad and sandwhich bar for people to choose from. We need a poster to hang outside our door to let people know that we are now also serving aussie coffee and breakfast as well as our usual malaysian cuisine.

Target Market(s)

Office location

Industry/Entity Type

Restaurant

Font styles to use
Decorative
Script

Requirements
Must have
• images and word
Nice to have
• something bold to attract people's attention

```html
<!DOCTYPE html>
<html lang="en">
<head>
<meta charset="utf-8">
<title>Aussie Coffee &amp; Aussie Breakfast 7–11 AM</title>
<link rel="stylesheet" href="https://fonts.googleapis.com/css2?family=Barlow:wght@600;700;800&display=swap">
<style>
  :root {
    --poster-orange: #da8f1d;
    --ink: #111111;
    --chalk: #f5f5f5;
    --chalk-edge: #b9b9b9;
    --shadow-edge: #2a2a2a;
    --frame-dark: #2b2114;
    --frame-light: #f3e2c4;
  }
  html, body {
    margin: 0;
    padding: 0;
    width: 848px;
    height: 1200px;
    overflow: hidden;
    background: var(--poster-orange);
  }
  .poster {
    display: block;
    width: 848px;
    height: 1200px;
    font-family: "Barlow", "Arial", sans-serif;
  }
  .frame-outer { fill: none; stroke: var(--frame-dark); stroke-width: 1.5; }
  .frame-inner { fill: none; stroke: var(--frame-light); stroke-width: 1.5; }
  .headline { font-weight: 700; font-size: 64px; letter-spacing: 3px; }
  .headline--dark { fill: var(--ink); }
  .headline--light { fill: var(--chalk); }
  .ampersand { font-weight: 800; font-size: 118px; fill: var(--ink); }
  .hours { font-weight: 800; font-size: 300px; }
  .hours-depth { fill: var(--ink); stroke: var(--ink); stroke-width: 6; stroke-linejoin: round; }
  .hours-depth--edge { stroke: var(--shadow-edge); }
  .hours-face { fill: var(--chalk); stroke: var(--chalk-edge); stroke-width: 5; stroke-linejoin: round; paint-order: stroke; }
  .tagline { font-weight: 700; font-size: 37px; letter-spacing: 1.5px; }
  .tagline--dark { fill: var(--ink); }
  .tagline--light { fill: var(--chalk); }
</style>
</head>
<body>
<svg class="poster" viewBox="0 0 848 1200" xmlns="http://www.w3.org/2000/svg" role="img" aria-label="Aussie coffee and Aussie breakfast, 7 to 11 AM. Salad and sandwich bar, Malaysian cuisine all day.">
  <rect width="848" height="1200" fill="var(--poster-orange)"/>

  <path class="frame-outer" d="M66 30 H780 V76 H821 V1122 H780 V1166 H66 V1122 H27 V76 H66 Z"/>
  <rect class="frame-inner" x="41" y="48" width="766" height="1102"/>

  <text class="headline headline--dark" x="75" y="161" textLength="240" lengthAdjust="spacingAndGlyphs">AUSSIE</text>
  <text class="headline headline--dark" x="77" y="242" textLength="255" lengthAdjust="spacingAndGlyphs">COFFEE</text>
  <text class="ampersand" x="367" y="166" textLength="78" lengthAdjust="spacingAndGlyphs">&amp;</text>
  <text class="headline headline--light" x="510" y="161" textLength="240" lengthAdjust="spacingAndGlyphs">AUSSIE</text>
  <text class="headline headline--light" x="374" y="242" textLength="396" lengthAdjust="spacingAndGlyphs">BREAKFAST</text>

  <defs>
    <text id="hours-time" class="hours" x="242" y="569" textLength="428" lengthAdjust="spacingAndGlyphs">7-11</text>
    <text id="hours-period" class="hours" x="230" y="866" textLength="434" lengthAdjust="spacingAndGlyphs">AM</text>
  </defs>

  <g class="hours-depth hours-depth--edge">
    <use href="#hours-time" transform="translate(-65 28)"/>
    <use href="#hours-period" transform="translate(-65 28)"/>
  </g>
  <g class="hours-depth">
    <use href="#hours-time" transform="translate(-60 25.8)"/>
    <use href="#hours-time" transform="translate(-55 23.7)"/>
    <use href="#hours-time" transform="translate(-50 21.5)"/>
    <use href="#hours-time" transform="translate(-45 19.4)"/>
    <use href="#hours-time" transform="translate(-40 17.2)"/>
    <use href="#hours-time" transform="translate(-35 15.1)"/>
    <use href="#hours-time" transform="translate(-30 12.9)"/>
    <use href="#hours-time" transform="translate(-25 10.8)"/>
    <use href="#hours-time" transform="translate(-20 8.6)"/>
    <use href="#hours-time" transform="translate(-15 6.5)"/>
    <use href="#hours-time" transform="translate(-10 4.3)"/>
    <use href="#hours-time" transform="translate(-5 2.2)"/>
    <use href="#hours-period" transform="translate(-60 25.8)"/>
    <use href="#hours-period" transform="translate(-55 23.7)"/>
    <use href="#hours-period" transform="translate(-50 21.5)"/>
    <use href="#hours-period" transform="translate(-45 19.4)"/>
    <use href="#hours-period" transform="translate(-40 17.2)"/>
    <use href="#hours-period" transform="translate(-35 15.1)"/>
    <use href="#hours-period" transform="translate(-30 12.9)"/>
    <use href="#hours-period" transform="translate(-25 10.8)"/>
    <use href="#hours-period" transform="translate(-20 8.6)"/>
    <use href="#hours-period" transform="translate(-15 6.5)"/>
    <use href="#hours-period" transform="translate(-10 4.3)"/>
    <use href="#hours-period" transform="translate(-5 2.2)"/>
  </g>
  <g class="hours-face">
    <use href="#hours-time"/>
    <use href="#hours-period"/>
  </g>

  <text class="tagline tagline--dark" x="174" y="1041" textLength="480" lengthAdjust="spacingAndGlyphs">salad &amp; sandwhich bar</text>
  <text class="tagline tagline--light" x="154" y="1094" textLength="523" lengthAdjust="spacingAndGlyphs">malaysian cusine all day</text>
</svg>
</body>
</html>
```